Business Card Design

colour scheme is to be grey background and light green writing
i would like some kind of brick arch highlighted in green and the writing inside the arch in green also
on the back list..all types of brickwork, no job to small, free quote and space to write a small quote underneath

RMT Brickwork
0418562093
kelvorbest47@mailqorp.com

```html
<!DOCTYPE html>
<html lang="en">
<head>
<meta charset="utf-8">
<title>RMT Brickwork – Business Card</title>
<link rel="stylesheet" href="https://fonts.googleapis.com/css2?family=Josefin+Sans:wght@400;600;700&display=swap">
<style>
  :root {
    --page-bg: #e6e6e4;
    --card-bg: #2b2b2c;
    --green: #5fb63a;
    --white: #f4f4f4;
    --line-grey: #c9c9c9;
  }
  * { box-sizing: border-box; margin: 0; padding: 0; }
  html, body {
    width: 1200px; height: 889px; overflow: hidden;
    background: var(--page-bg);
    font-family: "Josefin Sans", sans-serif;
  }
  .sheet {
    width: 1200px; height: 889px;
    display: flex; align-items: center; justify-content: center; gap: 48px;
  }
  .card {
    position: relative;
    width: 530px; height: 303px;
    background: var(--card-bg);
    border-radius: 4px;
    box-shadow: 0 6px 18px rgba(0,0,0,.25);
    overflow: hidden;
  }

  /* back: services + quote */
  .quote-panel {
    position: absolute; left: 26px; top: 26px;
    width: 262px; height: 251px;
  }
  .quote-panel__title {
    position: absolute; left: 0; top: 0;
    font-size: 15px; font-weight: 700; letter-spacing: .5px;
    color: var(--white);
  }
  .quote-panel__title span { color: var(--green); }
  .quote-panel__box { position: absolute; left: 0; top: 24px; }

  .services {
    position: absolute; left: 306px; top: 28px; right: 18px;
  }
  .services__heading {
    font-size: 27px; font-weight: 700; letter-spacing: .5px;
    color: var(--green); line-height: 1; white-space: nowrap;
  }
  .services__list { list-style: none; margin-top: 14px; }
  .services__list li {
    position: relative; padding-left: 15px;
    font-size: 9.5px; font-weight: 600; letter-spacing: .5px;
    text-transform: uppercase; color: var(--white);
    line-height: 17px; white-space: nowrap;
  }
  .services__list li::before {
    content: ""; position: absolute; left: 0; top: 4px;
    width: 6px; height: 6px; background: var(--green);
  }
  .services__rule {
    position: absolute; left: 306px; right: 18px; top: 182px;
    height: 2px; background: var(--green);
  }
  .contact {
    position: absolute; left: 306px; right: 12px;
    display: flex; align-items: center; gap: 10px;
    color: var(--white); white-space: nowrap;
  }
  .contact svg { flex-shrink: 0; }
  .contact--phone { top: 198px; }
  .contact--email { top: 244px; }
  .contact__phone-number { font-size: 24px; font-weight: 600; letter-spacing: 1px; }
  .contact__email { font-size: 10px; font-weight: 600; letter-spacing: .3px; text-transform: uppercase; }

  /* front: name */
  .front__brand {
    position: absolute; left: 0; right: 0; top: 118px;
    display: flex; align-items: center; justify-content: center; gap: 14px;
  }
  .front__mark {
    width: 22px; height: 22px; border-radius: 50%; background: var(--green);
  }
  .front__name {
    font-size: 38px; font-weight: 700; letter-spacing: 1px;
    color: var(--green); text-transform: uppercase;
  }
  .front__web {
    position: absolute; right: 22px; bottom: 20px;
    font-size: 11px; font-weight: 600; letter-spacing: .8px;
    color: var(--white);
  }
</style>
</head>
<body>
<main class="sheet">

  <section class="card card--back" aria-label="Card back: services and free quote">
    <div class="quote-panel">
      <p class="quote-panel__title">FREE <span>QUOTE</span></p>
      <svg class="quote-panel__box" width="262" height="227" viewBox="0 0 262 227" aria-hidden="true">
        <path d="M0 0 H262 V197 L232 227 H0 Z" fill="#ffffff"/>
        <g stroke="#c9c9c9" stroke-width="1">
          <line x1="10" y1="28" x2="252" y2="28"/>
          <line x1="10" y1="56" x2="252" y2="56"/>
          <line x1="10" y1="84" x2="252" y2="84"/>
          <line x1="10" y1="112" x2="252" y2="112"/>
          <line x1="10" y1="140" x2="252" y2="140"/>
          <line x1="10" y1="168" x2="252" y2="168"/>
          <line x1="10" y1="196" x2="242" y2="196"/>
          <line x1="176" y1="140" x2="176" y2="220"/>
          <line x1="214" y1="140" x2="214" y2="220"/>
        </g>
      </svg>
    </div>

    <div class="services">
      <h2 class="services__heading">BRICKWORKS</h2>
      <ul class="services__list">
        <li>Common burnt clay bricks</li>
        <li>Sand lime bricks</li>
        <li>Engineering bricks</li>
        <li>Concrete bricks</li>
        <li>Fly ash clay bricks</li>
      </ul>
    </div>
    <div class="services__rule"></div>

    <div class="contact contact--phone">
      <svg width="22" height="28" viewBox="0 0 22 28" aria-hidden="true">
        <rect x="2" y="1" width="18" height="26" rx="3" fill="#5fb63a"/>
        <rect x="5" y="4" width="12" height="9" fill="#2b2b2c"/>
        <g fill="#2b2b2c">
          <rect x="5" y="16" width="3" height="2"/><rect x="9.5" y="16" width="3" height="2"/><rect x="14" y="16" width="3" height="2"/>
          <rect x="5" y="20" width="3" height="2"/><rect x="9.5" y="20" width="3" height="2"/><rect x="14" y="20" width="3" height="2"/>
        </g>
      </svg>
      <span class="contact__phone-number">0418562093</span>
    </div>
    <div class="contact contact--email">
      <svg width="24" height="17" viewBox="0 0 26 18" aria-hidden="true">
        <rect x="0" y="0" width="26" height="18" fill="#5fb63a"/>
        <path d="M1 1 L13 10 L25 1" fill="none" stroke="#2b2b2c" stroke-width="2"/>
      </svg>
      <span class="contact__email">kelvorbest47@mailqorp.com</span>
    </div>
  </section>

  <section class="card card--front" aria-label="Card front: company name">
    <div class="front__brand">
      <span class="front__mark" aria-hidden="true"></span>
      <h1 class="front__name">RMT Brickwork</h1>
    </div>
    <p class="front__web">www.rmtbuildco.com</p>
  </section>

</main>
</body>
</html>
```